High end boutique food product label

We are looking for a label design to be used on our range of high end food products. We don't have a design or colour scheme in mind and are interested to see what ideas are submitted.
We would like it to feel sophisticated, chic, and eye-catching.
All of our products are handmade in Australia using Australian ingredients.
The graphics for the label will need to be scaleable to be fit a variety of labels from small squat jars with labels sized 3.5cm high and 7cm wide, to tall thin bottles with labels that are 14cm high and 4.5cm wide.
We would be interested in working with the winning designer to create these different sized labels.
The label submitted for this project should be 14cm high and 4.5cm wide, it should include our logo (file supplied in .jpeg and .ai), the product name 'Extra Virgin Olive Oil' and the size '250ml'.
This is just the front label on a bottle, we are not expecting a rear label to be created currently.
You are welcome to use any fonts you think will look good but the fonts used in our logo are Allaina Medium and Bebas Kai Regular.

```html
<!DOCTYPE html>
<html lang="en">
<head>
<meta charset="utf-8">
<title>Extra Virgin Olive Oil – Label Range</title>
<link rel="stylesheet" href="https://fonts.googleapis.com/css2?family=Marcellus&family=Bebas+Neue&display=swap">
<style>
  :root {
    --backdrop: #eeeeec;
    --label-ink: #131a21;
    --label-ink-soft: #1d2125;
    --gold: #c4ab82;
    --gold-deep: #a8916b;
    --white: #ffffff;
  }
  * { box-sizing: border-box; margin: 0; padding: 0; }
  html, body {
    width: 1200px;
    height: 973px;
    overflow: hidden;
    background: var(--backdrop);
  }
  .range {
    position: relative;
    width: 1200px;
    height: 973px;
    display: flex;
    justify-content: center;
    align-items: center;
    gap: 120px;
  }
  .label {
    position: relative;
    width: 257px;
    height: 800px;
    background: var(--label-ink);
    overflow: hidden;
  }
  .key-band {
    position: absolute;
    left: 0;
    width: 100%;
    height: 10px;
    background: var(--gold-deep);
  }
  .key-band--top { top: 12px; }
  .key-band--bottom { top: 777px; }
  .key-band--band-top { top: 467px; }
  .key-band--band-bottom { top: 619px; }

  .foliage {
    position: absolute;
    left: 0;
    top: 200px;
    width: 100%;
    height: 575px;
    background: radial-gradient(ellipse at 55% 45%, var(--label-ink-soft) 0%, var(--label-ink) 70%);
  }
  .brand {
    position: absolute;
    top: 92px;
    left: 0;
    width: 100%;
    text-align: center;
    font-family: "Marcellus", serif;
    color: var(--white);
    font-size: 30px;
    line-height: 1.05;
  }
  .product-band {
    position: absolute;
    left: 0;
    top: 477px;
    width: 100%;
    height: 142px;
    display: flex;
    flex-direction: column;
    justify-content: center;
    align-items: center;
    font-family: "Marcellus", serif;
  }
  .label--gold .product-band {
    background: var(--gold);
    color: var(--label-ink);
  }
  .label--dark .product-band {
    background: var(--label-ink);
    color: var(--gold);
  }
  .product-band .variety {
    font-size: 27px;
    line-height: 1.1;
    margin-right: 12px;
  }
  .product-band .product {
    font-size: 48px;
    line-height: 1;
  }
  .volume {
    position: absolute;
    top: 738px;
    left: 0;
    width: 100%;
    text-align: center;
    font-family: "Bebas Neue", sans-serif;
    font-size: 14px;
    letter-spacing: 2px;
    color: var(--white);
  }
  .label--dark .volume {
    font-size: 18px;
    letter-spacing: 0.5px;
  }
</style>
</head>
<body>
<main class="range">

  <article class="label label--gold">
    <div class="key-band key-band--top" role="img" aria-label="Gold Greek key border"></div>
    <div class="foliage" role="img" aria-label="Faint olive branch illustration"></div>
    <p class="brand">R&amp;T<br>Fieldhouse</p>
    <div class="key-band key-band--band-top" role="img" aria-label="Gold Greek key border"></div>
    <div class="product-band">
      <span class="variety">Extra Virgin</span>
      <span class="product">Olive oil</span>
    </div>
    <div class="key-band key-band--band-bottom" role="img" aria-label="Gold Greek key border"></div>
    <p class="volume">250ML</p>
    <div class="key-band key-band--bottom" role="img" aria-label="Gold Greek key border"></div>
  </article>

  <article class="label label--dark">
    <div class="foliage" role="img" aria-label="Faint olive branch illustration"></div>
    <p class="brand">R&amp;T<br>Fieldhouse</p>
    <div class="key-band key-band--band-top" role="img" aria-label="Gold Greek key border"></div>
    <div class="product-band">
      <span class="variety">Extra Virgin</span>
      <span class="product">Olive oil</span>
    </div>
    <div class="key-band key-band--band-bottom" role="img" aria-label="Gold Greek key border"></div>
    <p class="volume">250ML</p>
  </article>

</main>
</body>
</html>
```